Drag Show Flyer

We are holding a Drag Show, we are looking for something fun and exciting, over the top is a must.

Show Date: Saturday September 2nd 2017
Venue: Pelican Row Cafe Bunbury
Doors open 7pm
Tickets: $50 per person, includes glass of sparkling on arrival and canapes
Tickets available at the Venue or from ticketloom.com.au

Target Market(s)

Female, Hens Party, LBGT

Industry/Entity Type

Entertainment

Colors

Designer to choose colors to be used in the design.

Requirements
Must have
• Show Date: Saturday September 2nd 2017
• Venue: Pelican Row Cafe Bunbury
• Doors open 7pm
• Tickets: $50 per person, includes glass of sparkling on arrival and canapes
• Tickets available at the Venue or from ticketloom.com.au

```html
<!DOCTYPE html>
<html lang="en">
<head>
<meta charset="utf-8">
<title>A Night with the Queens – Pelican Row Cafe</title>
<link rel="stylesheet" href="https://fonts.googleapis.com/css2?family=Bebas+Neue&family=Yellowtail&display=block">
<style>
  :root {
    --black: #000000;
    --red: #d41f26;
    --deep-red: #a8121a;
    --white: #ffffff;
    --grey: #555555;
    --ink: #1a1a1a;
  }
  * { margin: 0; padding: 0; box-sizing: border-box; }
  html, body { width: 849px; height: 1200px; overflow: hidden; background: var(--white); }
  .flyer {
    position: relative; width: 849px; height: 1200px; overflow: hidden;
    background: var(--white); font-family: "Bebas Neue", "Arial Narrow", sans-serif;
  }
  .top-bar { position: absolute; left: 0; top: 0; width: 849px; height: 120px; background: var(--black); }
  .venue-name {
    position: absolute; left: 34px; top: 38px; color: var(--white);
    font-size: 44px; line-height: 1; letter-spacing: 1px;
  }
  .tagline {
    position: absolute; left: 356px; top: 16px; color: var(--white);
    font-size: 40px; line-height: 42px; letter-spacing: 0.5px;
  }
  .boots-art {
    position: absolute; left: 28px; top: 120px; width: 420px; height: 490px;
    background: linear-gradient(160deg, #e0262e 0%, #b3121b 55%, #7a0a10 100%);
  }
  .date-block {
    position: absolute; left: 440px; top: 182px; width: 560px;
    transform: rotate(6deg); transform-origin: left top;
  }
  .band { color: var(--white); line-height: 1; white-space: nowrap; }
  .band-day { background: var(--black); height: 94px; padding: 10px 0 0 82px; font-size: 88px; }
  .band-date { background: var(--black); height: 100px; margin-top: 8px; padding: 10px 0 0 54px; font-size: 90px; margin-left: -12px; }
  .band-details { background: var(--red); height: 124px; margin-top: 8px; padding: 14px 0 0 52px; margin-left: -24px; }
  .band-details .time { font-size: 40px; padding-left: 40px; line-height: 40px; }
  .band-details .place { font-size: 27px; line-height: 27px; }
  .title-art {
    position: absolute; left: 0; top: 0; width: 849px; height: 1200px;
    pointer-events: none; overflow: hidden;
  }
  .title-text {
    font-family: "Yellowtail", "Pacifico", cursive;
    fill: var(--red); stroke: var(--white); stroke-width: 8px;
    paint-order: stroke; stroke-linejoin: round;
    filter: drop-shadow(3px 4px 3px rgba(0,0,0,0.28));
  }
  .performers {
    position: absolute; left: 324px; top: 852px; font-size: 34px; line-height: 38px;
    color: var(--ink); white-space: nowrap;
  }
  .performers .names { color: var(--red); }
  .tickets {
    position: absolute; left: 0; width: 849px; top: 952px; text-align: center;
    font-size: 35px; color: var(--grey); letter-spacing: 0.5px;
  }
  .footer-band {
    position: absolute; left: 0; top: 1016px; width: 849px; height: 184px;
    background: radial-gradient(circle at 40% 40%, #e1262f 0%, var(--red) 45%, var(--deep-red) 100%);
    color: var(--white);
  }
  .booking { position: absolute; left: 60px; top: 34px; font-size: 29px; line-height: 1;
             text-shadow: 2px 2px 2px rgba(0,0,0,0.35); white-space: nowrap; }
  .phone { position: absolute; left: 60px; top: 68px; font-size: 72px; line-height: 1;
           text-shadow: 3px 3px 3px rgba(0,0,0,0.35); white-space: nowrap; }
  .sponsors-label { position: absolute; left: 568px; top: 36px; font-size: 21px; line-height: 1; }
  .sponsor-badge { position: absolute; top: 66px; width: 72px; height: 72px; border-radius: 50%; background: var(--white); }
  .sponsor-one { left: 590px; }
  .sponsor-two { left: 674px; }
</style>
</head>
<body>
<div class="flyer">
  <header class="top-bar">
    <div class="venue-name">Pelican Row Cafe</div>
    <div class="tagline">A glittering night of<br>drag shows &amp; outrageous fun!</div>
  </header>

  <div class="boots-art" role="img" aria-label="Illustration of glossy red lace-up thigh-high stiletto boots"></div>

  <div class="date-block">
    <div class="band band-day">Saturday</div>
    <div class="band band-date">Sept 2, 2017</div>
    <div class="band band-details">
      <div class="time">From 7pm till late!</div>
      <div class="place">Pelican Row Cafe &amp; Restaurant<br>18 Harbourlight Drive, Bunbury</div>
    </div>
  </div>

  <svg class="title-art" viewBox="0 0 849 1200" aria-label="A night with the Queens">
    <text class="title-text" x="52" y="830" font-size="300" textLength="730" lengthAdjust="spacingAndGlyphs">Queens</text>
    <text class="title-text" x="296" y="668" font-size="88" textLength="462" lengthAdjust="spacingAndGlyphs">A night with the</text>
  </svg>

  <div class="performers">
    With fabulous shows by<br>
    <span class="names">Miss Dragqueen</span> &amp; <span class="names">Miss Dragqueen</span>
  </div>

  <div class="tickets">Tickets $50pp includes canapes &amp; bubbly on arrival!</div>

  <footer class="footer-band">
    <div class="booking">Book now at www.ticketloom.com.au or</div>
    <div class="phone">Phone 9721 5560</div>
    <div class="sponsors-label">Proudly brought to you by</div>
    <div class="sponsor-badge sponsor-one"></div>
    <div class="sponsor-badge sponsor-two"></div>
  </footer>
</div>
</body>
</html>
```